Redesign Company Website WRAPTIDE

We want to redesign the web page of the company using some actual pictures such as the ones that show the production line, equipment and the plant. About the products picture i am ok if upgrade for new ones o keep some of them.
PLease visiti: www.lumodiseno.example.ve/wraptide/ to check the actual page.

Target Market(s)

Processors and Producers of:
Cheese, Fresh Meat, Sausages, Poultry, Processed Meats,

Coding

Coded - Design and coding required

Number of Pages Required

5+ page

Requirements
Must have
• Bilingual Spanish/English
Nice to have

Should not have
• Blogs, or any customer interaction, no particular brand must be shown, must be all generic.

```html
<!DOCTYPE html>
<html lang="es">
<head>
<meta charset="utf-8">
<title>Wraptide · Contacto / Contact</title>
<link rel="stylesheet" href="https://fonts.googleapis.com/css2?family=Open+Sans:ital,wght@0,400;0,600;0,700;1,400&family=Overlock:ital,wght@1,400;1,700&display=swap">
<style>
  :root {
    --teal: #0aa39a;
    --lime: #8dc63f;
    --ink: #000000;
    --paper: #ffffff;
    --nav-active: #1a1a1a;
    --muted: #8a8a8a;
    --map-light: #eeeeee;
    --map-mid: #d9d9d9;
  }
  * { box-sizing: border-box; margin: 0; padding: 0; }
  html, body { width: 1200px; height: 722px; overflow: hidden; background: var(--ink); }
  body { position: relative; font-family: "Open Sans", Arial, sans-serif; }

  .site-header { position: absolute; left: 0; top: 0; width: 1200px; height: 32px; background: var(--paper); }
  .main-nav { position: absolute; left: 485px; top: 0; height: 32px; display: flex; align-items: center; gap: 18px; }
  .main-nav a { color: var(--teal); font-weight: 700; font-size: 12.5px; text-decoration: none; }
  .main-nav a.is-active { color: var(--nav-active); }

  .language-switch {
    position: absolute; left: 925px; top: 7px; height: 18px; display: flex;
    border: 1.5px solid var(--teal); border-radius: 9px; overflow: hidden;
  }
  .language-switch a {
    width: 30px; line-height: 15px; text-align: center; font-size: 10.5px; font-weight: 700;
    color: var(--teal); text-decoration: none;
  }
  .language-switch a.is-current { background: var(--teal); color: var(--paper); }

  .brand-tab {
    position: absolute; left: 165px; top: 32px; width: 198px; height: 80px;
    background: var(--paper); border-bottom-right-radius: 22px;
    display: flex; align-items: center; justify-content: center; gap: 8px;
  }
  .brand-mark { width: 12px; height: 12px; background: var(--teal); }
  .brand-name { color: var(--teal); font-weight: 700; font-size: 24px; letter-spacing: 1px; }

  .section-title {
    position: absolute; left: 170px; top: 142px; width: 180px; height: 35px;
    background: var(--lime); border-radius: 3px; color: var(--paper);
    font-size: 16.5px; font-weight: 400; padding-left: 36px; line-height: 35px;
  }

  .contact-list { position: absolute; left: 210px; top: 207px; width: 268px; list-style: none; }
  .contact-item {
    display: flex; align-items: center; gap: 12px; width: 268px; height: 53px; margin-bottom: 11px;
    border: 3px solid var(--teal); color: var(--teal);
    font-family: "Overlock", "Open Sans", sans-serif; font-style: italic; font-size: 14px; line-height: 19px;
    padding: 0 14px 0 18px;
  }
  .contact-item.is-tall { height: 77px; }
  .contact-item svg { flex: none; width: 18px; height: 18px; }

  .language-note {
    position: absolute; left: 210px; top: 494px; width: 268px; height: 145px;
    background: var(--lime); color: var(--paper); padding: 20px 22px;
    font-family: "Overlock", "Open Sans", sans-serif; font-style: italic; font-size: 15px; line-height: 21px;
  }
  .language-note strong { display: block; font-size: 16px; margin-bottom: 8px; }

  .visit-panel {
    position: absolute; left: 525px; top: 207px; width: 435px; height: 113px;
    border: 3px solid var(--teal); color: var(--teal);
    font-style: italic; font-size: 12.5px; line-height: 17px; text-align: center; padding-top: 25px;
  }
  .visit-panel .lang-en { color: var(--muted); }

  .location-map {
    position: absolute; left: 525px; top: 342px; width: 435px; height: 297px;
    background: linear-gradient(160deg, var(--map-light), var(--map-mid));
  }

  .site-footer { position: absolute; left: 165px; top: 701px; color: var(--muted); font-size: 11px; }
</style>
</head>
<body>
  <header class="site-header">
    <nav class="main-nav">
      <a href="#">Home</a>
      <a href="#">Nosotros</a>
      <a href="#">Mercados</a>
      <a href="#">Empaques</a>
      <a href="#">Interes</a>
      <a href="#" class="is-active">Contacto</a>
    </nav>
    <div class="language-switch" aria-label="Idioma / Language">
      <a href="#" class="is-current" aria-current="true" lang="es">ES</a>
      <a href="#" lang="en">EN</a>
    </div>
  </header>

  <div class="brand-tab">
    <span class="brand-mark"></span>
    <span class="brand-name">WRAPTIDE</span>
  </div>

  <h1 class="section-title">Contáctanos</h1>

  <ul class="contact-list">
    <li class="contact-item">
      <svg viewBox="0 0 18 18" fill="none" stroke="currentColor" stroke-width="1.6"><rect x="1.5" y="4" width="15" height="10"/><path d="M1.5 4.5 9 10l7.5-5.5"/></svg>
      ventas@marenquimica.example.ve
    </li>
    <li class="contact-item">
      <svg viewBox="0 0 18 18" fill="none" stroke="currentColor" stroke-width="1.6"><path d="M4 2h3l1.5 4-2 1.3a8 8 0 0 0 4.2 4.2L12 9.5l4 1.5v3a2 2 0 0 1-2 2A12 12 0 0 1 2 4a2 2 0 0 1 2-2z"/></svg>
      +58 261-555-0142
    </li>
    <li class="contact-item is-tall">
      <svg viewBox="0 0 18 18" fill="none" stroke="currentColor" stroke-width="1.6"><path d="M9 16.5s5.5-5.2 5.5-9.5a5.5 5.5 0 0 0-11 0c0 4.3 5.5 9.5 5.5 9.5z"/><circle cx="9" cy="7" r="2"/></svg>
      Calle 90 con Avenida 17<br>Zona Industrial Norte
    </li>
  </ul>

  <p class="language-note">
    <strong>Español · English</strong>
    Atendemos en español e inglés.<br>
    <span lang="en">We serve you in Spanish and English.</span>
  </p>

  <div class="visit-panel">
    Visite nuestra planta de producción<br>
    Lunes a viernes · 8:00 – 17:00<br>
    <span class="lang-en" lang="en">Visit our plant · Monday to Friday</span>
  </div>

  <div class="location-map" role="img" aria-label="Mapa de calles con la ubicación de la planta Wraptide marcada"></div>

  <footer class="site-footer">© 2020 Wraptide. Todos los derechos reservados</footer>
</body>
</html>
```